依頼詳細
TOPページのイメージは変更せずに、最近導入したVRでの物件紹介や販売物件のページを増やしたい。VRのコンテンツについては、URLを組み込めるので、自社でカスタマイズできるようにしてほしい。
また、現在のTOPページを超える斬新なデザインを提案していただければ採用も検討します。
サイトURL
http://k-r-t.example.jp
ページ数
2ページ
希望イメージ
シンプル 複雑
単色 カラフル
暗い 明るい
日常 高級
遊び心 厳粛
未来的 伝統的
女性的 男性的
希望する色
納品ファイル
補足説明
以前に別法人のロゴをコンペ形式で募集した内容です。
参考までに↓
https://www.sakuhinba.example.jp/work/detail/503927
依頼金額を99320円に変更して、延長しました。
提案者が少なすぎて残念に思っております。
漠然とし過ぎた依頼なのかもしれませんが、デザイン性だけでも比較してみたいのが理由です。
期限時間ギリギリで1件の応募で、キャンセルするにしても全額お一人だけに配分することが納得いきませんので、何人かに配分出来ればと思い延長させて頂きました。
同じ方からの度重なる提案は受け入れ難く思っております。
これぞという提案でご参加いただきますようご配慮くださいませ。
仙台の街並み等の風景は個人的に好きではありません。
仙台が本社ではありますが、商圏は全国ですのであまり仙台を意識しないデザインでお願いします。

細かい部分はさておき、私の好みをなんとなく汲み取って頂いたようなので選ばせていただきました。

ご提案頂いた皆様ありがとうございました。

```html
<!DOCTYPE html>
<html lang="ja">
<head>
<meta charset="utf-8">
<title>HOMEFIND 不動産</title>
<link rel="stylesheet" href="https://fonts.googleapis.com/css2?family=Noto+Sans+JP:wght@400;500;700;900&family=Roboto:wght@400;500;700;900&display=swap">
<style>
:root{
  --ink:#2a2a2a;
  --dark:#2f2f2f;
  --text:#444;
  --muted:#888;
  --line:#d6d6d6;
  --bg:#ececec;
  --white:#fff;
  --accent:#f39a00;
  --price:#e07b00;
}
*{box-sizing:border-box;margin:0;padding:0}
html,body{width:1200px;height:2552px;overflow:hidden}
body{font-family:"Noto Sans JP",sans-serif;color:var(--text);background:var(--bg);font-size:12px;position:relative}
a{color:inherit;text-decoration:none}

.site-header{height:118px;background:var(--white);position:relative}
.topbar{height:26px;padding:0 36px;display:flex;justify-content:space-between;align-items:center;font-size:10px;color:var(--muted);border-bottom:1px solid #eee}
.topbar ul{display:flex;list-style:none;gap:10px}
.brand{position:absolute;left:36px;top:52px;font-family:"Roboto",sans-serif;font-weight:900;font-size:32px;letter-spacing:1px;color:var(--ink)}
.global-nav{position:absolute;right:36px;top:50px;display:flex;list-style:none}
.global-nav li{width:104px;text-align:center;border-left:1px solid var(--line);padding:4px 0}
.global-nav li:last-child{border-right:1px solid var(--line)}
.global-nav .en{display:block;font-family:"Roboto",sans-serif;font-size:11px;letter-spacing:1px;color:var(--ink)}
.global-nav .ja{display:block;font-size:10px;color:var(--muted);margin-top:3px}

.hero{height:540px;background:linear-gradient(180deg,#9fb3c4 0%,#b8c4cc 35%,#8b949a 70%,#5f676c 100%)}

.container{width:900px;margin:50px auto 0;display:flex;gap:32px}
.sidebar{width:192px;flex:none}
.side-btn{display:flex;justify-content:space-between;align-items:center;height:50px;padding:0 16px;background:var(--dark);color:var(--white);font-weight:700;font-size:13px;margin-bottom:14px}
.side-links{list-style:none;margin-top:20px;border-top:1px solid var(--line)}
.side-links li{height:38px;line-height:38px;border-bottom:1px solid var(--line);padding-left:6px;font-size:12px;color:var(--ink)}
.side-links li::before{content:"";display:inline-block;width:5px;height:5px;border-top:1px solid var(--ink);border-right:1px solid var(--ink);transform:rotate(45deg);margin-right:10px;vertical-align:2px}

.main{width:676px}
.section-title{font-size:15px;font-weight:700;color:var(--ink);padding-bottom:12px;border-bottom:2px solid var(--ink);margin-bottom:18px}
.news{list-style:none;margin-bottom:50px}
.news li{display:flex;padding:16px 0;border-bottom:1px dotted var(--line);line-height:1.85;font-size:12px}
.news time{width:110px;flex:none;font-family:"Roboto",sans-serif;color:var(--ink)}

.props{display:flex;gap:17px;margin-bottom:44px}
.prop{width:214px}
.prop-img{height:172px;position:relative}
.tag{position:absolute;left:0;top:0;background:var(--accent);color:var(--white);font-size:10px;font-weight:700;padding:3px 8px}
.prop-addr{font-size:11px;margin-top:12px;color:var(--ink)}
.prop-price{font-family:"Roboto",sans-serif;font-weight:700;font-size:19px;color:var(--price);margin-top:4px}
.prop-price small{font-size:11px;font-family:"Noto Sans JP",sans-serif}

.cta{display:flex;gap:30px;margin-bottom:70px;position:relative}
.cta a{flex:1;height:64px;background:var(--dark);color:var(--white);display:flex;align-items:center;justify-content:center;gap:14px;font-size:17px;font-weight:700}
.badge{position:absolute;left:346px;top:-16px;width:44px;height:44px;border-radius:50%;background:var(--accent);color:var(--white);font-family:"Roboto",sans-serif;font-weight:700;font-size:11px;display:flex;align-items:center;justify-content:center}

.stores-wrap{width:900px;margin:0 auto;padding-left:224px}
.stores{background:#e2e2e2;padding:42px 60px;display:flex;gap:40px}
.store{flex:1;background:var(--white);padding:28px 22px 30px;text-align:center;box-shadow:0 2px 4px rgba(0,0,0,.08)}
.store h3{font-size:15px;color:var(--ink)}
.store .hours{display:inline-block;background:var(--accent);color:var(--white);font-size:9px;padding:2px 8px;margin:8px 0 16px}
.store-img{height:190px}
.store dl{text-align:left;font-size:10.5px;line-height:2.1;margin:16px 0 20px;display:grid;grid-template-columns:56px 1fr}
.store dt{color:var(--ink);font-weight:500}
.map-btn{display:flex;align-items:center;justify-content:center;gap:10px;height:34px;background:var(--dark);color:var(--white);font-size:11px;border-radius:2px}

.site-footer{position:absolute;left:0;top:2318px;width:1200px;height:234px;background:var(--ink);color:#ccc}
.foot-links{display:flex;justify-content:center;list-style:none;padding:16px 0;border-bottom:1px solid #555;font-size:11px}
.foot-links li{padding:0 14px;border-right:1px solid #777}
.foot-links li:last-child{border-right:0}
.foot-body{width:900px;margin:34px auto 0;display:flex;justify-content:space-between;align-items:center}
.foot-brand{font-family:"Roboto",sans-serif;font-weight:900;font-size:30px;color:var(--white);letter-spacing:1px}
.foot-addr{font-size:10.5px;line-height:1.7;text-align:left}
.copyright{position:absolute;bottom:18px;width:100%;text-align:center;font-size:10px;color:#999;font-family:"Roboto",sans-serif}
</style>
</head>
<body>
<header class="site-header">
  <div class="topbar">
    <p>仲介手数料無料・賃貸物件のことならHOMEFIND</p>
    <ul><li>資料請求</li><li>|</li><li>ご利用上の注意</li><li>|</li><li>サイトマップ</li></ul>
  </div>
  <a class="brand" href="#">HOMEFIND</a>
  <ul class="global-nav">
    <li><span class="en">SEARCH</span><span class="ja">物件検索</span></li>
    <li><span class="en">HOW TO</span><span class="ja">賃貸物件の探し方</span></li>
    <li><span class="en">TO OWNERS</span><span class="ja">オーナー様へ</span></li>
    <li><span class="en">COMPANY</span><span class="ja">会社概要</span></li>
    <li><span class="en">CONTACT</span><span class="ja">お問い合わせ</span></li>
  </ul>
</header>

<div class="hero" role="img" aria-label="高層ビルが立ち並ぶ市街地の空撮写真"></div>

<div class="container">
  <aside class="sidebar">
    <a class="side-btn" href="#">物件検索<span>›</span></a>
    <a class="side-btn" href="#">VRで物件を見る<span>›</span></a>
    <ul class="side-links">
      <li>お部屋探しの手順</li>
      <li>オーナー様へ</li>
      <li>会社概要</li>
      <li>お問い合わせ</li>
      <li>求人情報</li>
    </ul>
  </aside>

  <main class="main">
    <h2 class="section-title">新着情報</h2>
    <ul class="news">
      <li><time>2019.03.31</time><p>GW休業期間のご案内<br>4月27日〜5月6日まで休業いたします。</p></li>
      <li><time>2019.03.19</time><p>新着賃貸物件のご案内<br>青葉区エリアに新しい賃貸物件を追加しました。ぜひご覧ください。<br>お問い合わせは営業時間内にお電話またはフォームよりどうぞ。</p></li>
      <li><time>2019.03.05</time><p>VR物件紹介を始めました<br>ご来店前にお部屋の様子をVRでご確認いただけます。<br>詳しくは「VRで物件を見る」ページをご覧ください。</p></li>
    </ul>

    <h2 class="section-title">おすすめ物件</h2>
    <div class="props">
      <div class="prop">
        <div class="prop-img" role="img" aria-label="マンション外観の写真" style="background:linear-gradient(180deg,#b9cde0,#9a8f80)"><span class="tag">売買物件</span></div>
        <p class="prop-addr">宮城県仙台市青葉区 北四番丁駅</p>
        <p class="prop-price">5,490<small>万円</small></p>
      </div>
      <div class="prop">
        <div class="prop-img" role="img" aria-label="マンション外観の写真" style="background:linear-gradient(180deg,#a9c4dc,#8c8c86)"><span class="tag">賃貸物件</span></div>
        <p class="prop-addr">宮城県仙台市青葉区 北四番丁駅</p>
        <p class="prop-price">95,000<small>円/月</small></p>
      </div>
      <div class="prop">
        <div class="prop-img" role="img" aria-label="一戸建て住宅外観の写真" style="background:linear-gradient(180deg,#bcd2e6,#a08a70)"><span class="tag">賃貸物件</span></div>
        <p class="prop-addr">宮城県仙台市青葉区 勾当台公園駅</p>
        <p class="prop-price">135,000<small>円/月</small></p>
      </div>
    </div>

    <div class="cta">
      <a href="#">物件検索<span>›</span></a>
      <span class="badge">NEW</span>
      <a href="#">VRで物件を見る<span>›</span></a>
    </div>

    <h2 class="section-title">店舗情報</h2>
  </main>
</div>

<div class="stores-wrap">
  <section class="stores">
    <article class="store">
      <h3>仙台本店</h3>
      <span class="hours">営業時間 10:00〜19:00</span>
      <div class="store-img" role="img" aria-label="店舗内観の写真" style="background:linear-gradient(180deg,#6e5a48,#3e342c)"></div>
      <dl>
        <dt>電話番号</dt><dd>022-555-0148</dd>
        <dt>FAX</dt><dd>022-555-0149</dd>
        <dt>営業時間</dt><dd>10:00〜19:00</dd>
        <dt>定休日</dt><dd>水・年末年始</dd>
      </dl>
      <a class="map-btn" href="#">MapLinkで見る
        <svg width="10" height="10" viewBox="0 0 10 10"><path d="M3 1l4 4-4 4" fill="none" stroke="#fff" stroke-width="1.4"/></svg></a>
    </article>
    <article class="store">
      <h3>大阪店</h3>
      <span class="hours">営業時間 10:00〜19:00</span>
      <div class="store-img" role="img" aria-label="店舗内観の写真" style="background:linear-gradient(180deg,#8a8684,#3d3a38)"></div>
      <dl>
        <dt>電話番号</dt><dd>06-5550-0192</dd>
        <dt>FAX</dt><dd>06-5550-0193</dd>
        <dt>営業時間</dt><dd>10:00〜19:00</dd>
        <dt>定休日</dt><dd>水・年末年始</dd>
      </dl>
      <a class="map-btn" href="#">MapLinkで見る
        <svg width="10" height="10" viewBox="0 0 10 10"><path d="M3 1l4 4-4 4" fill="none" stroke="#fff" stroke-width="1.4"/></svg></a>
    </article>
  </section>
</div>

<footer class="site-footer">
  <ul class="foot-links">
    <li>トップページ</li><li>会社概要</li><li>プライバシーポリシー</li><li>ご利用上の注意</li><li>お問い合わせ</li>
  </ul>
  <div class="foot-body">
    <span class="foot-brand">HOMEFIND</span>
    <p class="foot-addr">株式会社ホームファインド<br>〒980-0000 宮城県仙台市青葉区一番町1-2-3<br>TEL 022-555-0148 FAX 022-555-0149</p>
  </div>
  <p class="copyright">Copyright @ k-r-t.example.jp All Rights Reserved.</p>
</footer>
</body>
</html>
```